Tobin Quartz Portal Page . It's guarantee project!

We need a clean and professional modern web application portal page
That includes the Login & Application Selection screen

Also, I need to design both Desktop and Mobile sizes.
We have an example design for our target

The application is Jetty Schedule and related data.
Our client is a bit conservative.

Theme color preferred : #00508B (main) #DF0D83 (secondary)

Target Market(s)

Oil & Fuel & Gasoline

Number of Pages Required

2 page

Font styles to use
Sans Serif

Colors
0054AA
0677BA
7BADD7
CADEEF
E8F1F8
E54698
E96AAD
F1A4CE
F9D9EA
FCEFF6

Requirements
Must have
• Login Page & Main Screen

```html
<!DOCTYPE html>
<html lang="en">
<head>
<meta charset="utf-8">
<title>Tobin Quartz – Jetty Scheduling Portal</title>
<link href="https://fonts.googleapis.com/css2?family=Rubik:wght@300;400;500;700&display=swap" rel="stylesheet">
<style>
  :root{
    --page:#f6f7f9;
    --navy:#0a2a6e;
    --blue-deep:#0d3387;
    --blue:#1f4fb5;
    --blue-light:#3b6fd0;
    --sea:#0b4b86;
    --pink:#e0127f;
    --pink-soft:#e96aad;
    --pink-pale:#fcf0f6;
    --ink:#1d1d27;
    --muted:#8aa3d6;
    --link:#0677ba;
    --line:#cfd3da;
    --white:#ffffff;
  }
  *{box-sizing:border-box;margin:0;padding:0}
  html,body{width:902px;height:1200px;overflow:hidden}
  body{background:var(--page);font-family:"Rubik",sans-serif;color:var(--ink);position:relative}
  .board{position:absolute;overflow:hidden;box-shadow:0 4px 14px rgba(20,40,90,.12)}
  .scene{position:absolute;inset:0;
    background:
      radial-gradient(ellipse 45% 60% at 75% 65%, rgba(40,110,150,.55), transparent 70%),
      radial-gradient(ellipse 30% 40% at 85% 85%, rgba(70,120,90,.35), transparent 70%),
      linear-gradient(160deg,var(--blue-light) 0%,var(--blue) 30%,var(--blue-deep) 65%,var(--navy) 100%);}
  .abs{position:absolute}

  /* login */
  .brand{display:flex;align-items:center;gap:5px;color:var(--white);font-weight:700}
  .brand i{display:block;background:var(--white);border-radius:2px}
  .accent-block{position:absolute;background:var(--pink-soft);opacity:.92}
  .frame{position:absolute;border:2px solid var(--white)}
  .login-card{position:absolute;background:var(--white);padding:0}
  .login-card h2{position:absolute;left:15px;top:23px;font-size:11px;font-weight:500}
  .login-card h3{position:absolute;left:15px;top:49px;font-size:8.5px;font-weight:500}
  .login-card label{position:absolute;left:15px;font-size:6.5px}
  .field{position:absolute;left:15px;height:16px;border:1px solid var(--line);border-radius:2px}
  .row{position:absolute;left:15px;top:147px;display:flex;justify-content:space-between;align-items:center;font-size:6.5px}
  .row a{color:var(--link);text-decoration:none}
  .remember{display:flex;align-items:center;gap:6px}
  .remember i{width:9px;height:9px;border:1px solid var(--line);border-radius:2px;display:block}
  .btn{position:absolute;background:var(--pink);color:var(--white);border-radius:3px;display:flex;align-items:center;justify-content:center;font-size:7.5px}
  .status{position:absolute;left:15px;top:7px;right:8px;display:flex;justify-content:space-between;color:var(--white);font-size:7px;font-weight:500}
  .homebar{position:absolute;left:54px;width:61px;height:2px;border-radius:1px;background:rgba(255,255,255,.35)}

  /* home */
  .nav{position:absolute;left:25px;top:8px;right:25px;height:16px;display:flex;align-items:center;color:var(--white)}
  .nav .links{position:absolute;left:95px;display:flex;gap:14px;font-size:7px;color:var(--muted)}
  .nav .links b{color:var(--white);font-weight:500}
  .user{position:absolute;right:0;top:-2px;display:flex;align-items:center;gap:6px;text-align:right}
  .user strong{display:block;font-size:7px;font-weight:500}
  .user small{display:block;font-size:4.5px;color:var(--muted)}
  .avatar{width:16px;height:16px;border-radius:50%;background:#c9b4a6;border:1px solid var(--white)}
  .bell{position:absolute}
  .hero-title{position:absolute;color:var(--white);font-weight:700;font-size:19.5px;line-height:22px}
  .stat{position:absolute;width:57px;height:42px;background:var(--pink-pale);padding:7px 0 0 10px}
  .stat b{display:block;font-size:15px;font-weight:700;line-height:16px}
  .stat span{display:block;font-size:7.5px;margin-top:2px}
  .module{position:absolute;width:129px;height:149px;background:var(--white)}
  .module svg{position:absolute;left:14px;top:14px}
  .module h4{position:absolute;left:14px;top:48px;font-size:7px;font-weight:500;letter-spacing:.1px}
  .module ul{position:absolute;left:19px;top:66px;right:15px;list-style:none}
  .module li{height:15px;display:flex;align-items:center;font-size:6.3px;position:relative;padding-left:5px}
  .module li::before{content:"";position:absolute;left:0;width:2px;height:2px;border-radius:50%;background:var(--ink)}
  .module li span{margin-left:auto;color:var(--pink);font-size:7px}
  .m-navy{position:absolute;left:0;right:0;top:369px;bottom:0;background:var(--navy)}
</style>
</head>
<body>

<!-- Desktop login -->
<section class="board" style="left:33px;top:65px;width:616px;height:346px">
  <div class="scene" role="img" aria-label="Aerial photo of a loaded container ship at sea"></div>
  <div class="brand abs" style="left:87px;top:124px;font-size:16px"><i style="width:14px;height:14px"></i>Tobin Quartz</div>
  <div class="abs" style="left:87px;top:174px;color:#fff;font-size:24px;font-weight:700">Jetty Scheduling</div>
  <div class="abs" style="left:87px;top:208px;color:#fff;font-size:24px;font-weight:300">We sync your productivity</div>
  <div class="accent-block" style="left:379px;top:55px;width:108px;height:78px"></div>
  <div class="frame" style="left:474px;top:222px;width:107px;height:77px"></div>
  <div class="login-card" style="left:399px;top:75px;width:163px;height:207px">
    <h2>Welcome</h2>
    <h3>Log in to your account</h3>
    <label style="top:68px">Email Address or Username</label>
    <div class="field" style="top:81px;width:133px"></div>
    <label style="top:107px">Password</label>
    <div class="field" style="top:120px;width:133px"></div>
    <div class="row" style="width:133px"><a href="#">Forgot password?</a><span class="remember"><i></i>Remember me</span></div>
    <div class="btn" style="left:15px;top:163px;width:133px;height:22px">Login</div>
  </div>
</section>

<!-- Mobile login -->
<section class="board" style="left:700px;top:55px;width:169px;height:366px">
  <div class="scene" role="img" aria-label="Aerial photo of a container ship at sea"></div>
  <div class="status"><span>9:41</span>
    <svg width="28" height="6" viewBox="0 0 28 6"><rect x="0" y="4" width="1.5" height="2" fill="#fff"/><rect x="2.5" y="3" width="1.5" height="3" fill="#fff"/><rect x="5" y="1.5" width="1.5" height="4.5" fill="#fff"/><path d="M10 3a4 4 0 0 1 6 0M11.5 4.5a2 2 0 0 1 3 0" stroke="#fff" stroke-width="1" fill="none"/><rect x="19" y="1" width="8" height="4.5" rx="1" fill="#fff"/></svg>
  </div>
  <div class="brand abs" style="left:8px;top:43px;font-size:10px"><i style="width:9px;height:9px"></i>Tobin Quartz</div>
  <div class="abs" style="left:8px;top:69px;color:#fff;font-size:11px;font-weight:700">Jetty Scheduling</div>
  <div class="abs" style="left:8px;top:83px;color:#fff;font-size:11px;font-weight:300">We sync your productivity</div>
  <div class="accent-block" style="left:0;top:112px;width:108px;height:77px"></div>
  <div class="frame" style="left:61px;top:254px;width:104px;height:133px;border-color:var(--navy)"></div>
  <div class="login-card" style="left:8px;top:120px;width:154px;height:208px">
    <h2>Welcome</h2>
    <h3>Log in to your account</h3>
    <label style="top:68px">Email Address or Username</label>
    <div class="field" style="top:81px;width:125px"></div>
    <label style="top:107px">Password</label>
    <div class="field" style="top:120px;width:125px"></div>
    <div class="row" style="width:125px"><a href="#">Forgot password?</a><span class="remember"><i></i>Remember me</span></div>
    <div class="btn" style="left:15px;top:163px;width:125px;height:22px">Login</div>
  </div>
  <div class="homebar" style="top:361px"></div>
</section>

<!-- Desktop home -->
<section class="board" style="left:33px;top:490px;width:616px;height:346px">
  <div class="scene" role="img" aria-label="Aerial photo of a loaded container ship at sea"></div>
  <nav class="nav">
    <div class="brand" style="font-size:9px;font-weight:400"><i style="width:8px;height:8px"></i>Tobin Quartz</div>
    <div class="links"><b>Home</b><span>Schedules</span><span>Report</span></div>
    <svg class="bell" style="left:445px;top:1px" width="13" height="13" viewBox="0 0 13 13"><path d="M2 9.5h8l-1-1.5V5.5a3 3 0 0 0-6 0V8z" fill="#fff"/><circle cx="6" cy="11" r="1.2" fill="#fff"/><circle cx="9.5" cy="3" r="2.6" fill="#e5303b"/><text x="9.5" y="4.4" font-size="3.6" text-anchor="middle" fill="#fff" font-family="Rubik,sans-serif">5</text></svg>
    <div class="user"><div><strong>Marla Venn</strong><small>marla@tobinquartz.com</small></div><div class="avatar"></div></div>
  </nav>
  <div class="hero-title" style="left:77px;top:60px">Jetty work on your<br>scheduling</div>
  <div class="btn" style="left:77px;top:114px;width:98px;height:21px">Discover More</div>
  <div class="stat" style="left:351px;top:76px"><b>17</b><span>Inbound</span></div>
  <div class="stat" style="left:416px;top:76px"><b>23</b><span>Outbound</span></div>
  <div class="stat" style="left:481px;top:76px"><b>9</b><span>Shifting</span></div>

  <div class="module" style="left:104px;top:167px">
    <svg width="23" height="22" viewBox="0 0 23 22"><rect x="1" y="2" width="18" height="17" rx="1" fill="#fff" stroke="#2b2b3a"/><rect x="1" y="2" width="18" height="4" fill="#7badd7" stroke="#2b2b3a"/><g fill="#e96aad"><rect x="4" y="8" width="2.5" height="2"/><rect x="8" y="8" width="2.5" height="2"/></g><g fill="#7badd7"><rect x="12" y="8" width="2.5" height="2"/><rect x="4" y="12" width="2.5" height="2"/><rect x="8" y="12" width="2.5" height="2"/></g><circle cx="18" cy="17" r="4" fill="#e96aad" stroke="#2b2b3a"/><path d="M16 17l1.5 1.5 2.5-3" stroke="#fff" fill="none"/></svg>
    <h4>JETTY PLANNING</h4>
    <ul><li>Ship Schedule<span>→</span></li><li>Scheduling<span>→</span></li><li>Jetty Mapping<span>→</span></li><li>Ship Information<span>→</span></li><li>Planning Report<span>→</span></li></ul>
  </div>
  <div class="module" style="left:244px;top:167px">
    <svg width="23" height="22" viewBox="0 0 23 22"><path d="M8 18h8a3 3 0 0 0 0-6h-4a3 3 0 0 1 0-6h6" stroke="#2b2b3a" fill="none"/><path d="M19 1a2.5 2.5 0 0 1 2.5 2.5c0 2-2.5 4-2.5 4s-2.5-2-2.5-4A2.5 2.5 0 0 1 19 1z" fill="#e0127f"/><rect x="1" y="13" width="7" height="5" fill="#7badd7" stroke="#2b2b3a"/><circle cx="3" cy="19" r="1.2" fill="#2b2b3a"/><circle cx="7" cy="19" r="1.2" fill="#2b2b3a"/></svg>
    <h4>JETTY TRACKING</h4>
    <ul><li>Ship Tracking<span>→</span></li><li>Ship Status<span>→</span></li><li>Estimated Arrival Time<span>→</span></li><li>Weather Information<span>→</span></li><li>Notification and Alert<span>→</span></li></ul>
  </div>
  <div class="module" style="left:383px;top:167px">
    <svg width="23" height="22" viewBox="0 0 23 22"><rect x="1" y="1" width="21" height="20" rx="1" fill="#fff" stroke="#2b2b3a"/><rect x="1" y="1" width="21" height="3" fill="#7badd7" stroke="#2b2b3a"/><path d="M5 7h13M5 10h9" stroke="#2b2b3a"/><path d="M4 20a7.5 7.5 0 0 1 15 0z" fill="#f9d9ea" stroke="#2b2b3a"/><path d="M11.5 20l3-4" stroke="#e0127f"/></svg>
    <h4>JETTY PERFORMANCE</h4>
    <ul><li>Performance Dashboard<span>→</span></li><li>Performance Report<span>→</span></li><li>Capacity Analysis<span>→</span></li><li>Benchmarking<span>→</span></li><li>Feedback and Review<span>→</span></li></ul>
  </div>
</section>

<!-- Mobile home -->
<section class="board" style="left:700px;top:450px;width:169px;height:691px">
  <div class="scene" role="img" aria-label="Aerial photo of a container ship at sea" style="bottom:322px"></div>
  <div class="m-navy"></div>
  <div class="status"><span>9:41</span>
    <svg width="28" height="6" viewBox="0 0 28 6"><rect x="0" y="4" width="1.5" height="2" fill="#fff"/><rect x="2.5" y="3" width="1.5" height="3" fill="#fff"/><rect x="5" y="1.5" width="1.5" height="4.5" fill="#fff"/><path d="M10 3a4 4 0 0 1 6 0M11.5 4.5a2 2 0 0 1 3 0" stroke="#fff" stroke-width="1" fill="none"/><rect x="19" y="1" width="8" height="4.5" rx="1" fill="#fff"/></svg>
  </div>
  <div class="brand abs" style="left:8px;top:23px;font-size:6.5px;font-weight:400"><i style="width:6px;height:6px"></i>Tobin Quartz</div>
  <svg class="abs" style="left:60px;top:25px" width="12" height="7" viewBox="0 0 12 7"><path d="M0 1h12M0 6h12" stroke="#fff"/></svg>
  <svg class="bell" style="left:149px;top:23px" width="12" height="12" viewBox="0 0 13 13"><path d="M2 9.5h8l-1-1.5V5.5a3 3 0 0 0-6 0V8z" fill="#fff"/><circle cx="6" cy="11" r="1.2" fill="#fff"/><circle cx="9.5" cy="3" r="2.6" fill="#e5303b"/><text x="9.5" y="4.4" font-size="3.6" text-anchor="middle" fill="#fff" font-family="Rubik,sans-serif">1</text></svg>
  <div class="hero-title" style="left:8px;top:45px;font-size:19px">Jetty work on<br>your scheduling</div>
  <div class="btn" style="left:8px;top:99px;width:152px;height:21px">Discover More</div>
  <div class="stat" style="left:8px;top:143px;width:46px;padding-left:7px"><b>17</b><span>Inbound</span></div>
  <div class="stat" style="left:61px;top:143px;width:46px;padding-left:7px"><b>23</b><span>Outbound</span></div>
  <div class="stat" style="left:115px;top:143px;width:46px;padding-left:7px"><b>9</b><span>Shifting</span></div>

  <div class="module" style="left:20px;top:201px;height:148px">
    <svg width="23" height="22" viewBox="0 0 23 22"><rect x="1" y="2" width="18" height="17" rx="1" fill="#fff" stroke="#2b2b3a"/><rect x="1" y="2" width="18" height="4" fill="#7badd7" stroke="#2b2b3a"/><g fill="#e96aad"><rect x="4" y="8" width="2.5" height="2"/><rect x="8" y="8" width="2.5" height="2"/></g><g fill="#7badd7"><rect x="12" y="8" width="2.5" height="2"/><rect x="4" y="12" width="2.5" height="2"/><rect x="8" y="12" width="2.5" height="2"/></g><circle cx="18" cy="17" r="4" fill="#e96aad" stroke="#2b2b3a"/><path d="M16 17l1.5 1.5 2.5-3" stroke="#fff" fill="none"/></svg>
    <h4>JETTY PLANNING</h4>
    <ul><li>Ship Schedule<span>→</span></li><li>Scheduling<span>→</span></li><li>Jetty Mapping<span>→</span></li><li>Ship Information<span>→</span></li><li>Planning Report<span>→</span></li></ul>
  </div>
  <div class="module" style="left:20px;top:360px;height:148px">
    <svg width="23" height="22" viewBox="0 0 23 22"><path d="M8 18h8a3 3 0 0 0 0-6h-4a3 3 0 0 1 0-6h6" stroke="#2b2b3a" fill="none"/><path d="M19 1a2.5 2.5 0 0 1 2.5 2.5c0 2-2.5 4-2.5 4s-2.5-2-2.5-4A2.5 2.5 0 0 1 19 1z" fill="#e0127f"/><rect x="1" y="13" width="7" height="5" fill="#7badd7" stroke="#2b2b3a"/><circle cx="3" cy="19" r="1.2" fill="#2b2b3a"/><circle cx="7" cy="19" r="1.2" fill="#2b2b3a"/></svg>
    <h4>JETTY TRACKING</h4>
    <ul><li>Ship Tracking<span>→</span></li><li>Ship Status<span>→</span></li><li>Estimated Arrival Time<span>→</span></li><li>Weather Information<span>→</span></li><li>Notification and Alert<span>→</span></li></ul>
  </div>
  <div class="module" style="left:20px;top:520px;height:148px">
    <svg width="23" height="22" viewBox="0 0 23 22"><rect x="1" y="1" width="21" height="20" rx="1" fill="#fff" stroke="#2b2b3a"/><rect x="1" y="1" width="21" height="3" fill="#7badd7" stroke="#2b2b3a"/><path d="M5 7h13M5 10h9" stroke="#2b2b3a"/><path d="M4 20a7.5 7.5 0 0 1 15 0z" fill="#f9d9ea" stroke="#2b2b3a"/><path d="M11.5 20l3-4" stroke="#e0127f"/></svg>
    <h4>JETTY PERFORMANCE</h4>
    <ul><li>Performance Dashboard<span>→</span></li><li>Performance Report<span>→</span></li><li>Capacity Analysis<span>→</span></li><li>Benchmarking<span>→</span></li><li>Feedback and Review<span>→</span></li></ul>
  </div>
  <div class="homebar" style="top:686px"></div>
</section>

</body>
</html>
```